Save the date: email notification

I need a "Save the Date" email notification design for my wedding:

Objetives:

1.- to notify friends about our future wedding ( by sending an email)
2.- to request our friends to send us their phisical address. ( reply to the email)

It will not be the formal invitation for the wedding, just an announcement.

Wedding Date: 15-sep-2012
Our names: Lucía & Teodoro

Target Market(s)

friends, family and other commitments

Industry/Entity Type

Wedding

Requirements
Must have
• Wedding Date: 15-sep-2012
Our names: Lucía & Teodoro

```html
<!DOCTYPE html>
<html lang="en">
<head>
<meta charset="utf-8">
<title>Save the Date – Lucía &amp; Teodoro</title>
<link rel="stylesheet" href="https://fonts.googleapis.com/css2?family=Questrial&family=Cormorant+Garamond:wght@600;700&family=Archivo+Black&display=swap">
<style>
  :root {
    --navy: #0b3a5c;
    --gold: #a68a1c;
    --paper: #f8f3e6;
    --paper-glow: #fdfbf5;
    --white: #ffffff;
  }
  html, body {
    margin: 0;
    padding: 0;
    width: 1000px;
    height: 1200px;
    overflow: hidden;
    background: var(--paper);
  }
  .save-the-date {
    display: block;
    width: 1000px;
    height: 1200px;
  }
  .sans { font-family: "Questrial", "Century Gothic", sans-serif; }
  .serif { font-family: "Cormorant Garamond", "Goudy Old Style", serif; font-weight: 700; }
  .numeral { font-family: "Archivo Black", "Futura", sans-serif; }
  .navy-fill { fill: var(--navy); }
  .gold-fill { fill: var(--gold); }
  .white-fill { fill: var(--white); }
  .couple-names { font-family: "Cormorant Garamond", serif; font-weight: 700; letter-spacing: 2px; }
  .weekday { font-style: italic; }
  .rule-navy { stroke: var(--navy); }
  .rule-white { stroke: var(--white); }
  .ring { fill: none; stroke: var(--gold); stroke-width: 12; }
</style>
</head>
<body>
<svg class="save-the-date" viewBox="0 0 1000 1200" xmlns="http://www.w3.org/2000/svg" role="img" aria-label="Save the date for the wedding of Lucía and Teodoro, Saturday 15 September 2012">
  <defs>
    <radialGradient id="paper-glow" cx="50%" cy="45%" r="50%">
      <stop offset="0%" stop-color="var(--paper-glow)"/>
      <stop offset="100%" stop-color="var(--paper)"/>
    </radialGradient>
  </defs>

  <rect class="background" width="1000" height="1200" fill="url(#paper-glow)"/>

  <!-- Couple names -->
  <text class="couple-names navy-fill" x="500" y="165" font-size="40" text-anchor="middle">LUCÍA &amp; TEODORO</text>

  <!-- Announcement column -->
  <g class="announcement">
    <text class="sans navy-fill" x="50" y="358" font-size="42" textLength="608" lengthAdjust="spacingAndGlyphs">WE ARE GETTING MARRIED</text>

    <g class="invite-line">
      <circle class="gold-fill" cx="58" cy="395" r="8"/>
      <circle class="gold-fill" cx="80" cy="395" r="8"/>
      <text class="sans navy-fill" x="120" y="405" font-size="28" textLength="462" lengthAdjust="spacingAndGlyphs">AND WE LOVE YOU TO BE IN</text>
      <circle class="gold-fill" cx="612" cy="395" r="8"/>
      <circle class="gold-fill" cx="634" cy="395" r="8"/>
    </g>

    <text class="serif navy-fill" x="50" y="494" font-size="86" textLength="608" lengthAdjust="spacingAndGlyphs">OUR WEDDING</text>
    <text class="sans gold-fill" x="50" y="558" font-size="56" textLength="608" lengthAdjust="spacingAndGlyphs">WE HOPE YOU WILL</text>
    <text class="serif navy-fill" x="46" y="776" font-size="285" textLength="614" lengthAdjust="spacingAndGlyphs">SAVE</text>
    <text class="serif navy-fill" x="48" y="868" font-size="118" textLength="612" lengthAdjust="spacingAndGlyphs">THE DATE</text>
  </g>

  <!-- Divider -->
  <line class="rule-navy" x1="708" y1="296" x2="708" y2="911" stroke-width="8"/>

  <!-- Date column -->
  <g class="date-block">
    <text class="sans weekday navy-fill" x="849" y="360" font-size="38" text-anchor="middle" textLength="206" lengthAdjust="spacingAndGlyphs">SATURDAY</text>
    <line class="rule-navy" x1="745" y1="378" x2="953" y2="378" stroke-width="4"/>
    <text class="serif navy-fill" x="849" y="444" font-size="80" text-anchor="middle" textLength="208" lengthAdjust="spacingAndGlyphs">SEPT</text>
    <line class="rule-navy" x1="745" y1="462" x2="953" y2="462" stroke-width="4"/>
    <text class="numeral navy-fill" x="849" y="666" font-size="250" text-anchor="middle" textLength="212" lengthAdjust="spacingAndGlyphs">15</text>
    <line class="rule-navy" x1="745" y1="684" x2="953" y2="684" stroke-width="4"/>
    <text class="serif navy-fill" x="849" y="743" font-size="66" text-anchor="middle" textLength="186" lengthAdjust="spacingAndGlyphs">2012</text>
    <line class="rule-navy" x1="745" y1="755" x2="953" y2="755" stroke-width="4"/>

    <g class="wedding-rings">
      <circle class="ring" cx="808" cy="850" r="53"/>
      <circle class="ring" cx="892" cy="850" r="53"/>
    </g>
  </g>

  <!-- Reply request -->
  <g class="reply-band">
    <rect class="navy-fill" x="37" y="963" width="913" height="31"/>
    <rect class="navy-fill" x="37" y="997" width="913" height="82"/>
    <line class="rule-white" x1="59" y1="983" x2="443" y2="983" stroke-width="2"/>
    <text class="serif white-fill" x="500" y="989" font-size="22" text-anchor="middle" font-weight="600" letter-spacing="1">PLEASE,</text>
    <line class="rule-white" x1="557" y1="983" x2="941" y2="983" stroke-width="2"/>
    <text class="sans white-fill" x="68" y="1049" font-size="29" textLength="861" lengthAdjust="spacingAndGlyphs">REPLY TO THIS E-MAIL SENDING YOUR PHISICAL ADDRESS</text>
  </g>
</svg>
</body>
</html>
```